Business card and stationery design

Harbourlight Gatherings Co. is a leading event and conference design and management company.
Please view lumorahostgroup.com.au

The business cards needs to convey:
- professionalism and competency
- exclusivity
- memorable experiences and quality

The business card needs to have the following aspects:
- double sided
- Full colour CMYK
- Printed on either high gloss matt card (designer to recommend)

For the business stationery we require:
- Letterhead with top banner and bottom footer
- A thank you card design
- a with compliments slip design
- a MS powerpoint and MS publisher client presentation slide design which includes cover page and then a standard presentation page
(Note- we do NOT require an envelope design- who sends letters these days!)

The company image is using the key colours of gold, silver and black.
A black background to the business card has been used before and is preferred although we are open to options.

Target Market(s)

High end corporations and businesses that require their events and conferences to be exceptionally well designed and managed

Industry/Entity Type

Business

Contact Information for Business Card

FRONT:

Darian Whitlock
- Event and Conference Specialist

Mobile- +61 (0) 491 238 604
Office- 1300 617 482
dariannw@lumorahostgroup.com.au

Web- lumorahostgroup.com.au

BACK:

- Event and

Font styles to use
Other font styles liked:
• The logo designer used Trajan Pro Bold 3 for the font text in the logo

Requirements
Must have
• Amazing design of the following:
• - business card (double sided)
• - letterhead
• - client thank you card
• - powerpoint and publisher client presentation design files

```html
<!DOCTYPE html>
<html lang="en">
<head>
<meta charset="utf-8">
<title>Harbourlight Gatherings Co. — Business Card</title>
<link rel="stylesheet" href="https://fonts.googleapis.com/css2?family=Cinzel:wght@700&family=Open+Sans:wght@400;700&display=swap">
<style>
  :root {
    --page: #e9e6e0;
    --black: #0b0b0b;
    --gold: #d9a92c;
    --gold-light: #f3dc8e;
    --gold-deep: #c8921e;
    --silver: #cfcfd2;
    --ink: #1a1408;
    --white: #f5f5f5;
  }
  * { margin: 0; padding: 0; box-sizing: border-box; }
  html, body { width: 1200px; height: 950px; overflow: hidden; background: var(--page); }
  .sheet { position: relative; width: 1200px; height: 950px; }

  .card {
    position: absolute;
    width: 560px;
    height: 340px;
    border-radius: 4px;
    overflow: hidden;
    box-shadow: 0 10px 28px rgba(0,0,0,.28);
  }
  .card--front { left: 60px; top: 100px; background: var(--black); }
  .card--back  { left: 580px; top: 510px; }

  .brand-name {
    font-family: "Cinzel", serif;
    font-weight: 700;
    color: var(--white);
    letter-spacing: .04em;
    line-height: 1.15;
  }
  .rule { height: 2px; background: var(--gold); }

  /* front */
  .front-mark {
    position: absolute; right: 48px; top: 40px;
    width: 230px; height: 230px; border-radius: 50%;
    background: radial-gradient(circle at 40% 35%, var(--gold-light), var(--gold-deep));
  }
  .front-brand { position: absolute; left: 34px; top: 150px; width: 250px; }
  .front-brand .rule { width: 230px; margin-bottom: 10px; }
  .front-brand .brand-name { font-size: 22px; }
  .front-brand .rule--bottom { margin: 10px 0 10px; }
  .front-web {
    font-family: "Open Sans", sans-serif; font-size: 14px; color: var(--white); letter-spacing: .03em;
  }

  /* back */
  .back-art { position: absolute; inset: 0; }
  .back-brand { position: absolute; right: 30px; top: 44px; width: 230px; text-align: left; }
  .back-brand .mark {
    width: 26px; height: 26px; border-radius: 50%; background: var(--gold); margin-bottom: 10px;
  }
  .back-brand .brand-name { font-size: 17px; }
  .back-brand .rule { margin-top: 8px; width: 200px; }

  .contact {
    position: absolute; left: 34px; top: 150px;
    font-family: "Open Sans", sans-serif; color: var(--ink);
    font-size: 14px; line-height: 1.45;
  }
  .contact .name { font-size: 22px; font-weight: 700; line-height: 1.2; }
  .contact .role { margin-bottom: 6px; }
  .contact b { font-weight: 700; }
</style>
</head>
<body>
<main class="sheet">

  <section class="card card--front" aria-label="Business card front">
    <div class="front-mark" aria-hidden="true"></div>
    <div class="front-brand">
      <div class="rule"></div>
      <p class="brand-name">Harbourlight Gatherings Co.</p>
      <div class="rule rule--bottom"></div>
      <p class="front-web">www.lumorahostgroup.com.au</p>
    </div>
  </section>

  <section class="card card--back" aria-label="Business card back">
    <svg class="back-art" viewBox="0 0 560 340" width="560" height="340" aria-hidden="true">
      <defs>
        <linearGradient id="goldFace" x1="0" y1="1" x2="1" y2="0">
          <stop offset="0" stop-color="#c8921e"/>
          <stop offset=".45" stop-color="#f3dc8e"/>
          <stop offset="1" stop-color="#d9a92c"/>
        </linearGradient>
      </defs>
      <rect width="560" height="340" fill="url(#goldFace)"/>
      <path d="M250 0 C 205 110 270 230 560 250 L 560 0 Z" fill="#cfcfd2"/>
      <path d="M262 0 C 220 105 285 220 560 238 L 560 0 Z" fill="#0b0b0b"/>
    </svg>

    <div class="back-brand">
      <div class="mark" aria-hidden="true"></div>
      <p class="brand-name">Harbourlight Gatherings Co.</p>
      <div class="rule"></div>
    </div>

    <div class="contact">
      <p class="name">Darian Whitlock</p>
      <p class="role">Event &amp; Conference Specialist</p>
      <p><b>Mobile:</b> +61 (0) 491 238 604</p>
      <p><b>Phone:</b> 1300 617 482</p>
      <p>dariannw@lumorahostgroup.com.au</p>
      <p>www.lumorahostgroup.com.au</p>
    </div>
  </section>

</main>
</body>
</html>
```